A building General Contractor is looking for a business card design

I need a business card designed. The company "Crestline Structure Builders" is a general contractor for commercial buildings and pre-engineered metal buildings.

```html
<!DOCTYPE html>
<html lang="en">
<head>
<meta charset="UTF-8">
<title>Crestline Structure Builders – Business Card</title>
<link href="https://fonts.googleapis.com/css2?family=Open+Sans:wght@400;700&display=swap" rel="stylesheet">
<style>
  :root {
    --page-bg: #8e8e90;
    --card-bg: #2b2b2c;
    --card-back-bg: #262627;
    --text-main: #ffffff;
    --text-soft: #e6e6e6;
    --gloss-mark: #3c3c3e;
  }
  * { margin: 0; padding: 0; box-sizing: border-box; }
  html, body {
    width: 1200px; height: 801px; overflow: hidden;
    background: var(--page-bg);
    font-family: "Open Sans", sans-serif;
  }
  .stage {
    width: 1200px; height: 801px;
    display: flex; align-items: center; justify-content: center; gap: 40px;
  }
  .card {
    width: 540px; height: 309px;
    border-radius: 3px;
    box-shadow: 0 10px 28px rgba(0,0,0,0.35);
    position: relative;
  }
  .card--back {
    background: var(--card-back-bg);
    display: flex; align-items: center; justify-content: center;
  }
  .card--front { background: var(--card-bg); color: var(--text-main); }

  .brand-name {
    font-family: "Open Sans", sans-serif;
    font-weight: 700;
    text-transform: uppercase;
    letter-spacing: 1px;
    line-height: 1.1;
    display: flex; align-items: center; gap: 12px;
  }
  .brand-name__square { width: 14px; height: 14px; flex: none; }
  .card--back .brand-name { color: var(--gloss-mark); font-size: 26px; }
  .card--back .brand-name__square { background: var(--gloss-mark); }

  .card--front .brand-name {
    position: absolute; right: 40px; top: 70px;
    color: var(--text-main); font-size: 21px; width: 200px;
  }
  .card--front .brand-name__square { background: var(--text-main); }

  .contact-block { position: absolute; left: 48px; top: 118px; }
  .person-name { font-weight: 700; font-size: 19px; letter-spacing: 1px; text-transform: uppercase; }
  .person-title { font-size: 11.5px; color: var(--text-soft); margin-top: 2px; }
  .address { font-size: 14px; line-height: 1.35; margin-top: 24px; }
  .contact-list { list-style: none; margin-top: 18px; font-size: 14px; line-height: 1.35; }
  .contact-list li { display: flex; align-items: center; gap: 9px; }
  .contact-list svg { width: 11px; height: 11px; fill: var(--text-main); flex: none; }
</style>
</head>
<body>
<main class="stage">
  <section class="card card--back" aria-label="Card back">
    <div class="brand-name"><span class="brand-name__square"></span><span>Crestline Structure<br>Builders</span></div>
  </section>

  <section class="card card--front" aria-label="Card front">
    <div class="contact-block">
      <h1 class="person-name">Marcus Hallden</h1>
      <p class="person-title">Chief Executive Officer</p>
      <p class="address">1850 Ridgeview Ave.<br>Lakeport, TX 75000</p>
      <ul class="contact-list">
        <li><svg viewBox="0 0 24 24"><path d="M6.6 10.8a15.1 15.1 0 0 0 6.6 6.6l2.2-2.2a1 1 0 0 1 1-.25 11.4 11.4 0 0 0 3.6.57 1 1 0 0 1 1 1V20a1 1 0 0 1-1 1A17 17 0 0 1 3 4a1 1 0 0 1 1-1h3.5a1 1 0 0 1 1 1c0 1.25.2 2.45.57 3.57a1 1 0 0 1-.25 1z"/></svg>(555) 318-2046</li>
        <li><svg viewBox="0 0 24 24"><path d="M2 5h20v14H2z M2 5l10 8 10-8" /></svg>marcus@csb-build.com</li>
        <li><svg viewBox="0 0 24 24"><circle cx="12" cy="12" r="10"/></svg>www.csb-build.com</li>
      </ul>
    </div>
    <div class="brand-name"><span class="brand-name__square"></span><span>Crestline Structure<br>Builders</span></div>
  </section>
</main>
</body>
</html>
```